Calloway Ridge Associates Stationery

Use attached logo for stationery
Stationery, Letterhead and Envelope + Business cards

Tag line: Walking alongside those doing the work of the Gospel

```html
<!DOCTYPE html>
<html lang="en">
<head>
<meta charset="utf-8">
<title>Calloway Ridge Associates Stationery</title>
<link rel="stylesheet" href="https://fonts.googleapis.com/css2?family=Cinzel:wght@500&family=Open+Sans:wght@400;600;700&display=swap">
<style>
  :root {
    --navy: #0b4f8b;
    --sky: #5fd3ee;
    --sun: #fcc60a;
    --paper: #f6f6f7;
    --backdrop: #e8e8e9;
    --ink: #4a4a4a;
    --body-ink: #6e6e6e;
  }
  * { margin: 0; padding: 0; box-sizing: border-box; }
  html, body { width: 1200px; height: 825px; overflow: hidden; }
  body {
    background: var(--backdrop);
    position: relative;
    font-family: "Open Sans", Arial, sans-serif;
    color: var(--ink);
  }
  .sheet { position: absolute; background: var(--paper); overflow: hidden; }

  /* brand name block */
  .brand { position: absolute; display: flex; align-items: center; gap: 7px; }
  .brand-dot { width: 12px; height: 12px; border-radius: 50%; background: var(--sun); flex: none; }
  .brand-name {
    font-family: "Cinzel", Georgia, serif; font-weight: 500; color: var(--navy);
    font-size: 15px; line-height: 1.1; letter-spacing: .3px;
  }

  /* footer band */
  .band { position: absolute; left: 0; right: 0; bottom: 0; background: var(--sun); }
  .band-address { position: absolute; font-size: 7px; color: #3d3d3d; white-space: nowrap; }
  .band-address strong { font-weight: 700; }
  .url-tab {
    position: absolute; width: 130px; background: var(--navy); color: #fff;
    border-radius: 0 0 14px 14px; font-size: 7.5px; letter-spacing: .6px;
    display: flex; align-items: flex-end; justify-content: center; padding-bottom: 5px;
  }

  /* letterhead */
  .letterhead { left: 81px; top: 82px; width: 467px; height: 660px; }
  .letterhead .brand { left: 34px; top: 48px; }
  .contact { position: absolute; left: 339px; top: 43px; font-size: 7.2px; line-height: 9.6px; color: #444; }
  .contact li { list-style: none; display: flex; align-items: center; gap: 3px; }
  .contact svg { width: 6px; height: 6px; fill: var(--navy); }
  .salutation { position: absolute; left: 38px; top: 135px; font-size: 11px; font-weight: 700; color: #4c4c4c; }
  .letter-body { position: absolute; left: 38px; top: 163px; width: 392px; }
  .letter-body p {
    font-size: 9.3px; line-height: 12.2px; color: var(--body-ink);
    text-align: justify; margin-bottom: 12.2px;
  }
  .signature {
    position: absolute; left: 38px; top: 460px; width: 90px; height: 42px;
    background: linear-gradient(90deg, #d9d9dc, #ececee); border-radius: 4px;
  }
  .letterhead .band { height: 22px; }
  .letterhead .band-address { left: 30px; top: 7px; }
  .letterhead .url-tab { left: 308px; top: 622px; height: 33px; }

  /* compliment slip */
  .slip { left: 616px; top: 201px; width: 466px; height: 200px; }
  .slip .brand { left: 32px; top: 54px; }
  .slip .band { height: 22px; }
  .slip .band-address { left: 32px; top: 7px; }
  .slip .url-tab { left: 308px; top: 161px; height: 34px; }

  /* envelope */
  .envelope { left: 585px; top: 509px; width: 536px; height: 234px; }
  .envelope-flap { position: absolute; left: 585px; top: 441px; width: 536px; height: 69px; }
  .envelope-flap path { fill: var(--navy); }
  .envelope .brand { left: 27px; top: 56px; }
  .envelope .band { height: 22px; }
  .envelope .band-address { left: 39px; top: 7px; }
  .envelope .url-tab { left: 362px; top: 194px; height: 35px; }
</style>
</head>
<body>

  <!-- Letterhead -->
  <section class="sheet letterhead">
    <div class="brand">
      <span class="brand-dot"></span>
      <span class="brand-name">Calloway Ridge<br>Associates</span>
    </div>
    <ul class="contact">
      <li><svg viewBox="0 0 10 10"><path d="M2 0 L4 2.5 L3 3.8 Q4.5 6 6.2 7 L7.5 6 L10 8 L8.5 10 Q3 9 0 1.5 Z"/></svg>555-214-0178</li>
      <li><svg viewBox="0 0 10 10"><path d="M0 2 H10 V8 H0 Z M0 2 L5 5.5 L10 2" /></svg>info@callowayridge.com</li>
      <li><svg viewBox="0 0 10 10"><circle cx="5" cy="5" r="5"/></svg>www.callowayridge.com</li>
    </ul>
    <p class="salutation">Dear Mr. Doyle,</p>
    <div class="letter-body">
      <p>Lorem Ipsum is simply dummy text of the printing and typesetting industry. Lorem Ipsum has been the industry's standard dummy text ever since the 1500s, when an unknown printer took a galley of type and scrambled it to make a type specimen book. It has survived not only five centuries, but also the leap into electronic typesetting, remaining essentially unchanged.</p>
      <p>The standard chunk of Lorem Ipsum used since the 1500s is reproduced below for those interested. Sections 1.10.32 and 1.10.33 from "de Finibus Bonorum et Malorum" by Marcus Lenn are also reproduced in their exact original form, accompanied by English versions from the 1914 translation by H. Penwright</p>
      <p>Lorem Ipsum is simply dummy text of the printing and typesetting industry. Lorem Ipsum has been the industry's standard dummy text ever since the 1500s, when an unknown printer took a galley of type and scrambled it to make a type specimen book. It has survived not only five centuries, but also the leap into electronic typesetting, remaining essentially unchanged. It was popularised in the</p>
      <p>Lorem Ipsum is simply dummy text of the printing and typesetting industry. Lorem Ipsum has been the industry's standard dummy text ever since the 1500s, when an unknown printer took a galley of type and scrambled it to make a type specimen book. It has survived not only five centuries, but also the leap into electronic typesetting, remaining essentially unchanged. It was popularised in the</p>
    </div>
    <div class="signature" role="img" aria-label="Handwritten signature of the letter's sender"></div>
    <div class="band">
      <p class="band-address"><strong>Calloway Ridge Associates</strong> Po. box 201, Street Name, City Name, Zip Code - 00000</p>
    </div>
    <div class="url-tab">www.callowayridge.com</div>
  </section>

  <!-- Compliment slip -->
  <section class="sheet slip">
    <div class="brand">
      <span class="brand-dot"></span>
      <span class="brand-name">Calloway Ridge<br>Associates</span>
    </div>
    <div class="band">
      <p class="band-address"><strong>Calloway Ridge Associates</strong> Po. box 201, Street Name, City Name, Zip Code - 00000</p>
    </div>
    <div class="url-tab">www.callowayridge.com</div>
  </section>

  <!-- Envelope -->
  <svg class="envelope-flap" viewBox="0 0 536 69" aria-hidden="true">
    <path d="M0 69 L9 42 Q13 34 40 31 L248 2 Q268 -1 288 2 L500 31 Q525 34 529 42 L536 69 Z"/>
  </svg>
  <section class="sheet envelope">
    <div class="brand">
      <span class="brand-dot"></span>
      <span class="brand-name">Calloway Ridge<br>Associates</span>
    </div>
    <div class="band">
      <p class="band-address"><strong>Calloway Ridge Associates</strong> Po. box 201, Street Name, City Name, Zip Code - 00000</p>
    </div>
    <div class="url-tab">www.callowayridge.com</div>
  </section>

</body>
</html>
```